Bday party

UPDATED: Club flyer for Velvet's four year anniversary (main) and my birthday party (secondary). I have photos and logos. I will include a copy of a flyer I recently had done through artfolkhub.com that was perfect and i purchased it (ember mondays). I really like modern designs with a non-slutty girl. The girl is not mandatory though if it looks better without. Here is the text (also I attached a flyer for the main room of the club):

Velvet Nightclub's Four Year Anniversary

Also celebrating
KORVAN' BDAY

Pure House Music on the patio featuring
KORVAN
DELMA

Saturday 11/17 10p-2a

Congrats to the Newlyweds Trevor and Lorna (Pelham)!
Updates

I changed the focus from my bday to Velvet's four year anniversary so that is the main focus.  The non-slutty girl is not mandatory, it can be just graphics if that looks better.  I really like the sample flyer I attached as well.  Thanks.  

Industry/Entity Type

Club

Requirements
Should not have
• Anything too sexual (a cute girl on the flyer is fine but nothing too sexy)

```html
<!DOCTYPE html>
<html lang="en">
<head>
<meta charset="utf-8">
<title>Velvet Nightclub Four Year Anniversary</title>
<link href="https://fonts.googleapis.com/css2?family=Audiowide&family=Aldrich&family=Russo+One&display=swap" rel="stylesheet">
<style>
  :root {
    --night: #040306;
    --chrome: #f2f2f4;
    --chrome-shade: #9a9aa2;
    --violet: #7a2cff;
    --blue: #2a3cff;
    --neon-green: #3dff4f;
    --red: #ff2a2a;
    --guest-grey: #d8d8e0;
  }
  html, body { margin: 0; padding: 0; overflow: hidden; background: var(--night); }
  .flyer {
    position: relative;
    width: 853px;
    height: 1200px;
    overflow: hidden;
    background:
      radial-gradient(ellipse 380px 520px at 700px 640px, rgba(122,44,255,0.55), transparent 70%),
      linear-gradient(90deg, transparent 45%, rgba(42,60,255,0.18) 70%, rgba(122,44,255,0.25) 100%),
      var(--night);
    font-family: "Aldrich", sans-serif;
    color: var(--chrome);
  }
  .light-streaks {
    position: absolute; left: 440px; top: 200px; width: 413px; height: 760px;
    background: repeating-linear-gradient(90deg, rgba(60,90,255,0) 0 28px, rgba(90,60,255,0.22) 30px 34px, rgba(60,90,255,0) 36px 60px);
    filter: blur(2px);
  }
  .model-photo {
    position: absolute; left: 0; top: 110px; width: 490px; height: 1090px;
    background:
      radial-gradient(ellipse 150px 210px at 150px 320px, rgba(196,140,110,0.75), transparent 75%),
      radial-gradient(ellipse 260px 420px at 170px 840px, rgba(170,170,180,0.55), transparent 75%),
      linear-gradient(180deg, #2a1810 0%, #3a2418 40%, #1c1c22 70%, #0a0a0c 100%);
    -webkit-mask-image: linear-gradient(90deg, #000 70%, transparent 100%);
            mask-image: linear-gradient(90deg, #000 70%, transparent 100%);
  }
  .brand-title {
    position: absolute; left: 240px; top: 2px; margin: 0;
    font-family: "Audiowide", sans-serif; font-weight: 400;
    line-height: 0.86; text-transform: uppercase; color: var(--chrome);
    text-shadow: 0 2px 0 var(--chrome-shade);
  }
  .brand-title .word-top { display: block; font-size: 104px; letter-spacing: 4px; }
  .brand-title .word-bottom { display: block; font-size: 70px; letter-spacing: 2px; margin-top: 2px; }
  .anniversary {
    position: absolute; left: 240px; top: 166px; width: 505px; text-align: center;
    font-family: "Aldrich", sans-serif; font-size: 25px; letter-spacing: 3px;
    text-transform: uppercase; color: var(--chrome);
  }
  .presents {
    position: absolute; left: 588px; top: 208px;
    font-family: "Aldrich", sans-serif; font-size: 30px; letter-spacing: 1px; color: #fff;
  }
  .also-celebrating {
    position: absolute; left: 460px; top: 318px; width: 320px; text-align: center;
    font-family: "Aldrich", sans-serif; font-size: 22px; letter-spacing: 2px;
    text-transform: uppercase; color: var(--neon-green);
  }
  .speaker { position: absolute; left: 379px; top: 358px; width: 396px; height: 396px; }
  .headline {
    position: absolute; left: 205px; top: 372px; width: 640px; margin: 0;
    font-family: "Russo One", sans-serif; font-weight: 400; text-align: center;
    text-transform: uppercase; line-height: 1.02; color: var(--chrome);
    text-shadow: 4px 6px 0 var(--violet), 7px 10px 0 var(--blue);
  }
  .headline span { display: block; font-size: 140px; letter-spacing: 2px; }
  .headline .second { padding-left: 90px; }
  .patio-line {
    position: absolute; left: 180px; top: 736px;
    font-family: "Aldrich", sans-serif; font-size: 25px; text-transform: uppercase;
    color: var(--neon-green); letter-spacing: 0.5px;
  }
  .lineup {
    position: absolute; left: 406px; top: 790px; display: flex; align-items: center; gap: 10px;
    font-family: "Russo One", sans-serif; text-transform: uppercase;
  }
  .lineup .dj-main { font-size: 48px; color: var(--red); }
  .lineup .amp { font-size: 48px; color: var(--neon-green); }
  .lineup .dj-guest { font-family: "Aldrich", sans-serif; font-size: 40px; color: var(--guest-grey); letter-spacing: 3px; }
  .guest-ring {
    position: absolute; left: 672px; top: 768px; width: 110px; height: 110px;
    border-radius: 50%; border: 2px solid rgba(255,255,255,0.28);
  }
  .info-band {
    position: absolute; display: flex; align-items: center; justify-content: center;
    background: linear-gradient(90deg, rgba(15,90,28,0.35), rgba(20,110,35,0.7) 50%, rgba(15,90,28,0.35));
    box-shadow: 0 0 28px rgba(61,255,79,0.35);
    border-radius: 10px; color: #fff; text-transform: uppercase;
    font-family: "Aldrich", sans-serif;
  }
  .date-band { left: 107px; top: 930px; width: 684px; height: 48px; font-size: 26px; letter-spacing: 1px; }
  .congrats-band {
    left: 182px; top: 1032px; width: 513px; height: 92px; font-size: 25px; line-height: 1.35;
    flex-direction: column; align-items: flex-start; padding-left: 24px; box-sizing: border-box;
  }
</style>
</head>
<body>
<div class="flyer">
  <div class="light-streaks"></div>
  <div class="model-photo" role="img" aria-label="Photo of a young woman wearing DJ headphones in a silver jacket, eyes closed"></div>

  <h1 class="brand-title">
    <span class="word-top">Velvet</span>
    <span class="word-bottom">Nightclub</span>
  </h1>
  <div class="anniversary">Four Year Anniversary</div>
  <div class="presents">PRESENTS</div>

  <svg class="speaker" viewBox="0 0 396 396" role="img" aria-label="Illustration of a loudspeaker cone">
    <defs>
      <radialGradient id="speakerFill" cx="50%" cy="50%" r="50%">
        <stop offset="0%" stop-color="#3a3a40"/>
        <stop offset="70%" stop-color="#1e1e22"/>
        <stop offset="100%" stop-color="#0c0c0e"/>
      </radialGradient>
    </defs>
    <circle cx="198" cy="198" r="196" fill="url(#speakerFill)"/>
  </svg>

  <div class="also-celebrating">Also celebrating</div>
  <h2 class="headline">
    <span class="first">Korvan'</span>
    <span class="second">Bday</span>
  </h2>

  <div class="patio-line">Pure House Music on the Patio Featuring</div>

  <div class="guest-ring"></div>
  <div class="lineup">
    <span class="dj-main">Korvan</span>
    <span class="amp">&amp;</span>
    <span class="dj-guest">Delma</span>
  </div>

  <div class="info-band date-band">Saturday 11/17/12 10p-2a</div>
  <div class="info-band congrats-band">
    <span>Congrats to the Newlyweds</span>
    <span>Trevor and Lorna (Pelham)!</span>
  </div>
</div>
</body>
</html>
```